IT Distribution Wholesale Business Card & Logo Design

I need both logo and a business card that suits our business model, am happy to pay more for great effort put in.
Brevon Orbital Australia Pty Ltd
An IT Distribution / Wholesale company that distributes technology hardwares, softwares, components, etc.
Offer drop ship services for online retailers and supply to Australia-wide.
Based in Sydney Australia.
Design should give impressions of trust and stability.

Slogan: "your one stop technology supplier"
*two-sided name card
*logo + slogan on the back of the card

I don't have much specific requirements, leave it to designers to come up with creative & interesting masterpiece.
The logo and business card comes in first which i would like it to be completed latest by mid of March, we will require a whole redesign of our web pages, banner design, catalogue design later part.

Goodluck & thank you for your effort.

Hello designers,

Busy week, very good return rate on the number of designs and effort put into our business card design.
I thank you all for that.
We will have to extend this project for another week to two to receive more designs and more time for me to post some updates to you all.
We are getting there, i really liked some of the designs sent but just not the perfect masterpiece we are looking for.

Cheers,
Darnell Q.

Target Market(s)

Computer Retailers, Corporate, Schools, Councils.

Industry/Entity Type

Business

Requirements
Must have
• Brevon Orbital (Australia) Pty Ltd, Darnell Quist, Managing Director, Unit C, 14-18 Pellham Road, Dunmore NSW 2461, Ph +61 2 5037 1942, M +61 4 70395216, E darnell@brevonorbital.com.au, W www.brevonorbital.com.au
Nice to have
• Keep it simple & comfortable.
Target audiences are mostly >30-40 years old range.

Example of companies in the same line:-
http://www.kzp.com.au
http://www.norvix.com.au/
http://www.supplyhaventrade.com/
http://www.quenby.com.au/
http://www.bq456.com.au/
https://www.swiftgridhub.com.au/
http://carvelo.com.au/

```html
<!DOCTYPE html>
<html lang="en">
<head>
<meta charset="utf-8">
<title>Brevon Orbital Australia Pty Ltd – Business Card</title>
<link href="https://fonts.googleapis.com/css2?family=Arimo:wght@400;700&display=swap" rel="stylesheet">
<style>
  :root {
    --bg: #2b2b2d;
    --card-white: #f7f7f7;
    --band-light: #e9e9e9;
    --card-black: #060606;
    --band-dark: #141414;
    --band-teal: #24343a;
    --brand-blue: #1f8fd3;
    --ink-grey: #555a5e;
    --label-grey: #5d6266;
  }
  * { margin: 0; padding: 0; box-sizing: border-box; }
  html, body { width: 1200px; height: 900px; overflow: hidden; }
  body {
    background: var(--bg);
    font-family: "Arimo", Arial, sans-serif;
    display: flex;
    align-items: center;
    justify-content: center;
    gap: 40px;
  }
  .card {
    position: relative;
    width: 540px;
    height: 330px;
    overflow: hidden;
    border-radius: 2px;
  }
  .card-front { background: var(--card-white); }
  .card-back { background: var(--card-black); }

  .pattern-front {
    position: absolute;
    inset: 0;
    background: linear-gradient(180deg, var(--card-white) 0%, var(--band-light) 50%, var(--card-white) 100%);
  }
  .pattern-back {
    position: absolute;
    top: 0; right: 0; bottom: 0;
    width: 240px;
    background: linear-gradient(90deg, var(--card-black) 0%, var(--band-dark) 40%, var(--band-teal) 100%);
  }

  .wordmark {
    position: absolute;
    display: flex;
    flex-direction: column;
    align-items: flex-end;
  }
  .wordmark-row {
    display: flex;
    align-items: center;
    gap: 10px;
  }
  .wordmark-square {
    width: 22px; height: 22px;
    background: var(--brand-blue);
  }
  .wordmark-name {
    font-weight: 700;
    color: var(--brand-blue);
    font-size: 38px;
    letter-spacing: -0.5px;
    line-height: 1;
  }
  .wordmark-sub {
    font-size: 11px;
    color: var(--ink-grey);
    margin-top: 4px;
  }
  .card-front .wordmark { left: 70px; top: 132px; }
  .front-web {
    position: absolute;
    left: 0; right: 0; top: 246px;
    text-align: center;
    font-size: 11px;
    letter-spacing: 3px;
    color: #333;
  }

  .card-back .wordmark { left: 34px; top: 44px; }
  .card-back .wordmark-name { font-size: 30px; }
  .card-back .wordmark-square { width: 18px; height: 18px; }
  .card-back .wordmark-sub { color: #6d7478; font-size: 9px; }

  .contact { position: absolute; left: 34px; top: 122px; color: var(--brand-blue); }
  .contact-name { font-size: 24px; line-height: 1; }
  .contact-role { font-size: 12px; margin-top: 4px; }
  .contact-address { font-size: 12.5px; margin-top: 18px; line-height: 1.25; }
  .contact-lines { font-size: 12.5px; margin-top: 16px; line-height: 1.3; }
  .label { color: var(--label-grey); }
</style>
</head>
<body>

  <section class="card card-front" aria-label="Card front">
    <div class="pattern-front" role="img" aria-label="Light grey horizontal band pattern"></div>
    <div class="wordmark">
      <div class="wordmark-row">
        <span class="wordmark-square"></span>
        <span class="wordmark-name">Brevon Orbital</span>
      </div>
      <span class="wordmark-sub">Australia Pty Ltd</span>
    </div>
    <div class="front-web">www.brevonorbital.com.au</div>
  </section>

  <section class="card card-back" aria-label="Card back">
    <div class="pattern-back" role="img" aria-label="Dark horizontal band pattern with teal strips"></div>
    <div class="wordmark">
      <div class="wordmark-row">
        <span class="wordmark-square"></span>
        <span class="wordmark-name">Brevon Orbital</span>
      </div>
      <span class="wordmark-sub">Australia Pty Ltd</span>
    </div>
    <div class="contact">
      <div class="contact-name">Darnell Quist</div>
      <div class="contact-role">Managing Director</div>
      <div class="contact-address">Unit C, 14-18 Pellham Road,<br>Dunmore NSW 2461</div>
      <div class="contact-lines">
        <div><span class="label">P:</span> +61 2 5037 1942 <span class="label">M:</span> +61 4 70395216</div>
        <div><span class="label">E:</span> darnell@brevonorbital.com.au</div>
        <div><span class="label">W:</span> www.brevonorbital.com.au</div>
      </div>
    </div>
  </section>

</body>
</html>
```